C U B A N - C I G A R S - F L Y E R

I need a double-sided 5x7 club type flyer for a Memorial Day Weekend Trip.
The main side design needs to be similar to the attached flyer example. The front design of flyer is KEY. The design will be awarded to the closest finished submission to the example flyer.
Both sides of the flyer should also included event and business logo, which are also attached. Both logos can be altered to fit printing need accordingly.
Front side content is also attached.
The back side design will be very simple. Consists of 3 travel images and trip description, and my contact very details. Same color design as front. The attached word document contains backside details for REFERENCE ONLY. Please focus on front side when submitting a design for this project.
Target Market(s)
A F R I C A N - A M E R I C A N - C I G A R - S M O K E R S
Industry/Entity Type
Travel Industry
Requirements
Must have
- All the elements of the attached information
Nice to have
- Masculine Images
Should not have
- Large Cigar focus to catch customer's attention

```html
<!DOCTYPE html>
<html lang="en">
<head>
<meta charset="utf-8">
<title>Cuba Cigar Gentlemen's Memorial Day Weekend Flyer</title>
<link href="https://fonts.googleapis.com/css2?family=Titan+One&family=Nunito:wght@400;700;800&family=Yellowtail&display=swap" rel="stylesheet">
<style>
  :root {
    --backdrop: #e9e4dc;
    --gold: #c6a443;
    --gold-light: #d4b456;
    --brown-deep: #1e140c;
    --brown-dark: #3a2616;
    --brown-mid: #6e4c2c;
    --tobacco: #a57a4c;
    --cedar: #7a3a26;
    --red: #c4232b;
    --ink: #3a2818;
    --paper: #f7f2e6;
    --stripe: #1c1510;
  }
  * { margin: 0; padding: 0; box-sizing: border-box; }
  html, body { width: 1200px; height: 960px; overflow: hidden; }
  body {
    background: var(--backdrop);
    display: flex; align-items: center; justify-content: center;
    font-family: 'Nunito', sans-serif;
  }
  .flyer {
    position: relative;
    width: 1050px; height: 750px;
    display: flex;
    box-shadow: 0 10px 30px rgba(0,0,0,.25);
    overflow: hidden;
  }
  .flyer-photo {
    position: relative;
    flex: 1;
    background:
      radial-gradient(ellipse 45% 35% at 78% 78%, rgba(122,58,38,.85) 0%, rgba(122,58,38,0) 100%),
      radial-gradient(ellipse 55% 40% at 40% 45%, rgba(190,150,105,.75) 0%, rgba(165,122,76,0) 100%),
      linear-gradient(160deg, var(--brown-deep) 0%, var(--brown-dark) 18%, var(--brown-mid) 45%, var(--tobacco) 62%, var(--brown-mid) 82%, var(--brown-dark) 100%);
  }
  .business-mark {
    position: absolute; left: 70px; bottom: 70px;
    display: flex; align-items: center; gap: 14px;
    color: var(--paper);
    font-weight: 700;
    font-size: 24px; letter-spacing: 3px; text-transform: uppercase;
    opacity: .85;
  }
  .business-mark .ring {
    width: 30px; height: 30px; border-radius: 50%;
    border: 2px solid var(--paper);
  }
  .info-panel {
    position: relative;
    width: 395px;
    background: linear-gradient(180deg, var(--gold-light), var(--gold));
    border-left: 8px solid var(--paper);
    border-right: 26px solid var(--stripe);
    display: flex; flex-direction: column; align-items: center;
    padding: 44px 24px 40px;
    text-align: center;
    color: var(--ink);
  }
  .event-name {
    display: flex; align-items: center; gap: 12px;
    font-family: 'Titan One', sans-serif; font-size: 32px;
    color: var(--ink);
  }
  .event-name .dot {
    width: 26px; height: 26px; border-radius: 50%;
    background: var(--paper);
  }
  .event-dates {
    font-weight: 800; font-size: 20px; letter-spacing: 2px;
    color: var(--ink); margin: 6px 0 30px;
  }
  .headline {
    font-family: 'Titan One', sans-serif; font-weight: 400;
    text-transform: uppercase; line-height: 1.05;
  }
  .headline .lead { display: block; color: var(--red); font-size: 31px; }
  .headline .main { display: block; color: var(--ink); font-size: 34px; }
  .headline .tail { display: block; color: var(--red); font-size: 31px; }
  .tagline {
    font-family: 'Yellowtail', cursive; font-size: 24px; color: var(--ink);
    margin-top: 8px;
  }
  .divider {
    width: 88%; border: 0; border-top: 2px dotted var(--ink);
    margin: 18px 0;
  }
  .pitch { font-size: 23px; line-height: 1.2; }
  .pitch strong {
    display: block; font-family: 'Titan One', sans-serif; font-weight: 400;
    text-transform: uppercase; font-size: 23px;
  }
  .booking { font-size: 21px; line-height: 1.25; }
  .booking .url {
    display: block; color: var(--red); font-weight: 800; font-size: 19px;
  }
  .booking .call { display: block; font-size: 17px; margin-top: 6px; }
  .booking .phone {
    display: block; color: var(--red);
    font-family: 'Titan One', sans-serif; font-size: 27px; letter-spacing: 1px;
  }
</style>
</head>
<body>
  <main class="flyer">
    <section class="flyer-photo" role="img" aria-label="Photo: rows of premium cigars in a cedar humidor, a lit cigar with smoke, a glass of rum and bundled cigars">
      <div class="business-mark"><span class="ring"></span>Harbor Travel Co</div>
    </section>
    <aside class="info-panel">
      <div class="event-name"><span class="dot"></span>Island Escape</div>
      <p class="event-dates">MAY 25–28</p>
      <h1 class="headline">
        <span class="lead">A Cuba Cigar</span>
        <span class="main">Gentlemen's<br>Memorial</span>
        <span class="tail">Day Weekend</span>
      </h1>
      <p class="tagline">Cigars, Rum, &amp; Classic Cars...</p>
      <hr class="divider">
      <p class="pitch">Legally travel to Cuba<br>and return with real<strong>Cuban Cigars!</strong></p>
      <hr class="divider">
      <p class="booking">Book Today at
        <span class="url">EXAMPLETRIPS.com/HAVANA</span>
        <span class="call">For More Information Call:</span>
        <span class="phone">XXX-XXX-XXXX</span>
      </p>
    </aside>
  </main>
</body>
</html>
```